Australian Careers Business Needs 2 Banner Ad Design

We need a banner ad design for a new company based in Australia called Bright Sparrows. We provide career tools and insights to young professionals. Our target market is 20-30 year olds.

We would like to see designs that attract users on the site to click on the banner and sign up for a weekly newsletter. The newsletter will feature a blog, cheat sheets etc. Inspiration in their inbox!

The second banner is to attract users to sign up for a Horizon Gathering. They would click on it to find out more information and then register with their email address. This convention is a 1 day workshop designed to enhance young professionals abilities to give their best at work. There will CEO insights etc.

Use of images or flash is ok. Needs to look very professional and presented in accordance to the current colour scheme in place. Visit http://www.brightsparrows-demo.com/home to understand.

Banner sizes 300 x 250.
Mandatory use of Corporate Colours required on Font.
R66 G73 B74
R242 G240 B230
R38 G128 B138

No logo necessary.

Hi All,As both banners will feature on the Bright Sparrows site there is no need for a logo or hyperlink to the site.I would like to see some better images, and a bit more creative flair.Please don't use single female images as I am wanting to avoid the women in business perception. We cater to young professionals.Some suggestions for lines to utilise on the newsletter ad:Click here for weekly career tipsInvest in your career for free hereJoin the weekly conversationWeekly career tips in your inboxSign up for our weekly newsletterSome suggestions for lines to use on the horizon gathering ad:Register for the Horizon Gathering - Find out how to get ahead of your peersAre you a millennial climbing the corporate ladder? Find out how to rise to the topInterested in hearing from experts who recognise millennials are our future business leaders? Click here.Thanks,Megan Added Friday, April 3, 2015

Target Market(s)

20-30 years

Industry/Entity Type

Business

Font styles to use
Sans Serif

Requirements
Must have
• Please use images in the attached as options
Should not have
• NO LOGO - Its already onsite so not needed.

```html
<!DOCTYPE html>
<html lang="en">
<head>
<meta charset="utf-8">
<title>Bright Sparrows Banners</title>
<link rel="stylesheet" href="https://fonts.googleapis.com/css2?family=Alegreya:wght@400;500;700&display=swap">
<style>
  :root {
    --ink: #42494a;
    --cream: #f2f0e6;
    --teal: #26808a;
    --teal-mid: #43919c;
    --teal-soft: #5fa3ac;
    --teal-pale: #9ac5c9;
    --teal-mist: #7fb5bb;
    --slate: #7a7f80;
    --stone: #a9b3b4;
    --page: #ffffff;
  }
  html, body {
    margin: 0;
    padding: 0;
    width: 1200px;
    height: 770px;
    overflow: hidden;
    background: var(--page);
  }
  .canvas {
    position: relative;
    width: 1200px;
    height: 770px;
    font-family: "Alegreya", Georgia, serif;
  }
  .banner {
    position: absolute;
    display: block;
  }
  .banner--newsletter { left: 62px; top: 178px; }
  .banner--workshop { left: 621px; top: 176px; }
  .banner text { font-family: "Alegreya", Georgia, serif; }
  .headline-tag { font-size: 36px; fill: var(--cream); }
  .subline { font-size: 19px; fill: var(--teal); }
  .cta-label { font-size: 22px; fill: var(--cream); }
  .title { font-size: 37px; fill: var(--ink); }
  .lead { font-size: 25px; fill: var(--ink); }
  .event-name {
    font-size: 40px;
    font-weight: 700;
    fill: #ffffff;
    stroke: var(--ink);
    stroke-width: 5px;
    paint-order: stroke;
    stroke-linejoin: round;
  }
  .event-date { font-size: 19px; fill: var(--ink); }
  .values { font-size: 20px; fill: var(--ink); }
</style>
</head>
<body>
<main class="canvas">

  <svg class="banner banner--newsletter" width="496" height="414" viewBox="0 0 496 414" aria-label="Newsletter banner">
    <rect class="banner-bg" width="496" height="414" fill="var(--cream)"/>
    <polygon class="stripe stripe--dark" points="0,0 95,0 496,88 496,142 0,10" fill="var(--ink)"/>
    <polygon class="stripe stripe--teal" points="95,0 165,0 496,140 496,224" fill="var(--teal-mid)"/>

    <rect class="photo-area" x="28" y="90" width="214" height="186" rx="30" fill="url(#crowdTone)" role="img" aria-label="Photo of a group of young professionals standing together"/>
    <defs>
      <radialGradient id="crowdTone" cx="50%" cy="50%" r="60%">
        <stop offset="0%" stop-color="#6b6a6c"/>
        <stop offset="70%" stop-color="#a7a09c"/>
        <stop offset="100%" stop-color="var(--cream)"/>
      </radialGradient>
    </defs>

    <polygon class="ribbon ribbon--teal" points="26,407 454,330 372,244 300,262" fill="var(--teal)"/>
    <polygon class="ribbon ribbon--dark" points="0,357 356,237 428,322 0,400" fill="var(--ink)"/>
    <text class="headline-tag" x="12" y="385" transform="rotate(-17 12 385)">Be more intelligent..??</text>

    <text class="subline" x="130" y="404">get your newsletter for free</text>
    <circle class="cta" cx="440" cy="414" r="47" fill="var(--teal)"/>
    <text class="cta-label" x="440" y="405" text-anchor="middle">Find it</text>
  </svg>

  <svg class="banner banner--workshop" width="497" height="414" viewBox="0 0 497 414" aria-label="Workshop banner">
    <defs>
      <clipPath id="workshopClip"><rect width="497" height="414"/></clipPath>
    </defs>
    <g clip-path="url(#workshopClip)">
      <rect class="banner-bg" width="497" height="414" fill="var(--teal-pale)"/>
      <polygon class="header-band" points="0,0 497,0 497,78 0,50" fill="var(--cream)"/>

      <g class="diamonds">
        <polygon points="469,22 526,79 469,136 412,79" fill="var(--teal-soft)"/>
        <polygon points="354,132 411,189 354,246 297,189" fill="var(--teal-mist)"/>
        <polygon points="469,132 526,189 469,246 412,189" fill="var(--slate)"/>
        <polygon points="412,189 469,246 412,303 355,246" fill="var(--teal)"/>
        <polygon points="354,246 411,303 354,360 297,303" fill="var(--stone)"/>
        <polygon points="469,246 526,303 469,360 412,303" fill="var(--ink)"/>
        <polygon points="469,360 526,417 469,474 412,417" fill="var(--teal)"/>
      </g>

      <text class="title" x="22" y="42">One Day for Accelerate !!</text>
      <text class="lead" x="238" y="132" text-anchor="middle">Register Open Now</text>
      <text class="lead" x="238" y="165" text-anchor="middle">for</text>
      <text class="event-name" x="242" y="208" text-anchor="middle">Horizon Gathering</text>
      <text class="event-name" x="242" y="256" text-anchor="middle">Workshop</text>
      <text class="event-date" x="233" y="299" text-anchor="middle">June 7, 2015</text>
      <text class="values" x="38" y="402">Join • Improve • Success</text>
    </g>
  </svg>

</main>
</body>
</html>
```